Business Cards

Simple but professional looking business cards

Name: Rina Toskovar
Title: Principle Nexora Applications Consultant
Email: r@kldo.net.au
web : www.kldo.net.au
Phone: +61.8.92315547
Mobile: +61.438516622

Hi All, Please include the office address Level 1, 100 Bramwell St, West Perth, WA, 6005

```html
<!DOCTYPE html>
<html lang="en">
<head>
<meta charset="utf-8">
<title>KLDO Business Cards</title>
<link rel="stylesheet" href="https://fonts.googleapis.com/css2?family=Open+Sans:wght@400;600;700&display=swap">
<style>
  :root {
    --backdrop: #3a3a3c;
    --blue-deep: #0a5cae;
    --blue-mid: #0f86d6;
    --blue-light: #10b4ec;
    --brand-blue: #1a63b5;
    --accent-green: #8cc63f;
    --badge-red: #c4161c;
    --badge-grey: #d9d9d9;
    --paper: #ffffff;
    --ink-grey: #7d7d7d;
    --icon-blue: #1f5fa8;
  }
  * { margin: 0; padding: 0; box-sizing: border-box; }
  html, body { width: 1200px; height: 900px; overflow: hidden; }
  body {
    background: var(--backdrop);
    font-family: "Open Sans", Arial, sans-serif;
    position: relative;
  }
  .card {
    position: absolute;
    width: 600px;
    height: 343px;
    box-shadow: 0 6px 18px rgba(0,0,0,0.35);
  }
  /* Front side */
  .card-front {
    left: 130px;
    top: 70px;
    background: linear-gradient(35deg, var(--blue-light) 0%, var(--blue-mid) 45%, var(--blue-deep) 100%);
  }
  .front-brand {
    position: absolute;
    right: 40px;
    top: 168px;
    display: flex;
    align-items: center;
    gap: 12px;
  }
  .brand-dot {
    width: 34px;
    height: 34px;
    border-radius: 50%;
    flex: none;
  }
  .front-brand .brand-dot { background: var(--paper); }
  .front-brand .brand-name {
    color: var(--paper);
    font-weight: 600;
    font-size: 52px;
    letter-spacing: 1px;
    line-height: 1;
  }
  .partner-badge {
    position: absolute;
    right: 36px;
    top: 246px;
    width: 150px;
    height: 40px;
    background: linear-gradient(var(--badge-red) 0 55%, var(--badge-grey) 55% 100%);
    border-radius: 2px;
  }
  /* Back side */
  .card-back {
    left: 470px;
    top: 480px;
    background: var(--paper);
  }
  .back-brand {
    position: absolute;
    left: 44px;
    top: 40px;
    display: flex;
    align-items: center;
    gap: 12px;
  }
  .back-brand .brand-dot { background: var(--accent-green); }
  .back-brand .brand-name {
    color: var(--brand-blue);
    font-weight: 600;
    font-size: 52px;
    letter-spacing: 1px;
    line-height: 1;
  }
  .accent-bar {
    position: absolute;
    right: 0;
    top: 120px;
    width: 16px;
    height: 50px;
    background: var(--accent-green);
  }
  .holder {
    position: absolute;
    right: 44px;
    top: 124px;
    text-align: right;
  }
  .holder-name {
    color: var(--brand-blue);
    font-weight: 700;
    font-size: 21px;
    line-height: 1.2;
  }
  .holder-title {
    color: var(--ink-grey);
    font-size: 15px;
    line-height: 1.3;
  }
  .address {
    position: absolute;
    left: 44px;
    top: 178px;
    color: var(--ink-grey);
    font-size: 15px;
    line-height: 1.35;
  }
  .contact-list {
    position: absolute;
    left: 44px;
    top: 240px;
    list-style: none;
    color: var(--ink-grey);
    font-size: 15px;
  }
  .contact-list li {
    display: flex;
    align-items: center;
    gap: 12px;
    height: 22px;
  }
  .contact-list svg {
    width: 16px;
    height: 16px;
    fill: var(--icon-blue);
    flex: none;
  }
</style>
</head>
<body>
  <section class="card card-front" aria-label="Card front">
    <div class="front-brand">
      <span class="brand-dot"></span>
      <span class="brand-name">KLDO</span>
    </div>
    <div class="partner-badge"></div>
  </section>

  <section class="card card-back" aria-label="Card back">
    <div class="back-brand">
      <span class="brand-dot"></span>
      <span class="brand-name">KLDO</span>
    </div>
    <div class="accent-bar"></div>
    <div class="holder">
      <p class="holder-name">Rina Toskovar</p>
      <p class="holder-title">Principle Nexora Applications</p>
    </div>
    <p class="address">Level 1, 100 Bramwell St<br>West Perth, WA, 6005</p>
    <ul class="contact-list">
      <li>
        <svg viewBox="0 0 16 16" aria-hidden="true"><path d="M1 6c0-2 3-3 7-3s7 1 7 3v1h-4V6H5v1H1z"/><path d="M3 8h10l1 6H2z"/><circle cx="8" cy="11" r="1.6" fill="#fff"/></svg>
        +61.8.92315547
      </li>
      <li>
        <svg viewBox="0 0 16 16" aria-hidden="true"><path d="M4 1h8v14H4zM5.5 3v9h5V3z"/></svg>
        +61.438516622
      </li>
      <li>
        <svg viewBox="0 0 16 16" aria-hidden="true"><path d="M1 3h14v10H1zm1.5 1.5v.3L8 9l5.5-4.2v-.3zm0 2.2v4.8h11V6.7L8 10.9z"/></svg>
        r@kldo.net.au
      </li>
      <li>
        <svg viewBox="0 0 16 16" aria-hidden="true"><circle cx="8" cy="8" r="7"/><path d="M1 8h14M8 1v14M3 4h10M3 12h10" stroke="#fff" stroke-width="1" fill="none"/></svg>
        www.kldo.net.au
      </li>
    </ul>
  </section>
</body>
</html>
```